Homes, Invest in Non-performing loans

We need only 3 web pages, one for the home, one for the content, one for the properties.
The main focus of our business is to offer non performing loans (before foreclosures) to the general public. All the non-performing mortgages will end in a house, an apartment, a store, etc.
Our customers are able to invest from 10,000usd to 1,000,000usd (average 50,000usd).
Our customers' usual focus groups are employees who want second earnings, perceiving the business feeling without outlay time. They look for a solid finance sense corporation that confers them certainty.
Nearly all our clients desire the house, apartment, store, etc. more than the actual earnings.
The name of our company is BRAMLEY
Reason: We value the time and effort you already invest in our project. We realize that we did't come back on some of the doubts requested by the designers. It will be inequitable to the designers who prerequisite our feedback. We also appreciate the comprehension of the community in this postponement.
Reason: Designers,
We really apreciate all the time and effort you put on our project. From the begining we ask for 3 pages, so now we will leave the 10 finalist and provide some extra time to submit the other 2 pages.
We will race the price in 10%
Target Market(s)
Our customers average investors works as employees and want to have a second income or business without spending time. (People from 35 to 50)
Industry/Entity Type
Finance
Requirements
Should not have
- FLASH

```html
<!DOCTYPE html>
<html lang="en">
<head>
<meta charset="utf-8">
<title>Bramley — Non Performing Loans and Investment</title>
<link rel="stylesheet" href="https://fonts.googleapis.com/css2?family=Play:wght@400;700&family=Open+Sans:wght@400;600&family=Noto+Serif:ital@1&display=swap">
<style>
:root{
  --olive:#6e7a12;
  --ink:#1a1a1a;
  --text:#3f3f3f;
  --panel-top:#4a4d52;
  --panel-bottom:#050505;
  --footer:#2b2b2b;
  --white:#ffffff;
  --line:#d4d4d4;
}
*{margin:0;padding:0;box-sizing:border-box}
html,body{width:1200px;height:1181px;overflow:hidden;background:var(--white)}
body{position:relative;font-family:"Open Sans",sans-serif;color:var(--text)}

.hero{position:absolute;left:0;top:0;width:1200px;height:653px;
  background:linear-gradient(180deg,#e8e0c6 0%,#ddd3b0 40%,#b4ad78 62%,#97a052 80%,#aaa66a 100%);}

.masthead{position:absolute;left:120px;top:0;width:960px;height:110px;background:rgba(245,243,236,.55)}
.brand{position:absolute;left:28px;top:34px;display:flex;align-items:center;gap:8px;font-family:"Play",sans-serif;font-weight:700;font-size:26px;color:#2b2b2b;letter-spacing:1px}
.brand-mark{width:18px;height:18px;background:var(--olive)}
.phone{position:absolute;right:28px;top:20px;display:flex;align-items:center;gap:10px;font-size:17px;color:#222}
.search{position:absolute;right:24px;top:59px;width:194px;height:28px;border:1px solid #ccc;border-radius:14px;background:#fff;overflow:hidden}
.search span{position:absolute;left:13px;top:6px;font-size:11px;font-style:italic;color:#888}
.search-btn{position:absolute;right:0;top:0;width:30px;height:28px;background:#1b1b1b;display:flex;align-items:center;justify-content:center}

.nav{position:absolute;left:120px;top:109px;width:960px;height:48px;border-radius:6px 6px 0 0;background:linear-gradient(#3a3c40,#0c0c0c);border-bottom:6px solid var(--olive)}
.nav ul{list-style:none;display:flex;margin-left:18px;height:42px}
.nav li{font-size:13px;color:#fff;padding:0 22px;line-height:46px;margin-right:4px}
.nav li.active{background:var(--olive);margin-top:8px;line-height:30px;height:34px}

.hero-title{position:absolute;left:129px;top:298px;font-family:"Play",sans-serif;font-size:36px;line-height:43px;letter-spacing:-.6px;color:#111;font-weight:400}

.audiences{position:absolute;left:121px;top:581px;width:959px;height:194px;border-radius:5px;background:linear-gradient(var(--panel-top),var(--panel-bottom));display:flex;padding:16px 0 0 25px}
.audience{width:321px;color:#fff}
.audience h2{font-family:"Play",sans-serif;font-weight:400;font-size:25px;display:flex;align-items:center;gap:10px;height:34px}
.audience p{font-size:12.5px;line-height:16px;margin-top:14px;width:285px;letter-spacing:-.3px}
.read-more{display:flex;align-items:center;gap:8px;margin-top:26px;font-size:13px}

.welcome{position:absolute;left:136px;top:806px;width:555px}
.welcome h1{font-family:"Play",sans-serif;font-weight:400;font-size:29px;color:var(--ink);margin-left:-1px}
.welcome p{font-size:14.2px;line-height:21px;letter-spacing:-.15px;margin-top:17px;color:#444}
.welcome p + p{margin-top:21px}
.welcome h1 em{font-style:normal;color:var(--olive)}

.testimonials{position:absolute;left:740px;top:808px;width:329px;height:274px;border:1px solid var(--line);background:#f7f7f7;box-shadow:0 1px 2px rgba(0,0,0,.12);overflow:hidden}
.testimonials h3{height:43px;line-height:43px;padding-left:22px;font-size:17px;font-weight:600;color:#333;background:linear-gradient(#fff,#ececec);border-bottom:1px solid var(--line)}
.quote{padding:10px 10px 6px 20px;height:118px}
.quote + .quote{background:#f1f1f1;height:112px}
.person{display:flex;gap:14px}
.avatar{width:56px;height:56px;border:1px solid #ddd;background:#8a8f98}
.who{font-size:10.5px;line-height:20px;font-style:italic;color:#555}
.who b{font-weight:400;font-size:12.5px;color:#333}
.quote blockquote{font-family:"Noto Serif",serif;font-style:italic;font-size:11.5px;letter-spacing:-.35px;line-height:20px;color:#333;margin-top:6px}
.grip{position:absolute;left:150px;bottom:5px;width:30px;height:4px;border-top:1px dotted #999;border-bottom:1px dotted #999}

.footer{position:absolute;left:0;top:1125px;width:1200px;height:56px;background:var(--footer)}
.footer small{position:absolute;left:151px;top:20px;font-size:11.5px;color:#aaa}
.social{position:absolute;left:836px;top:16px;display:flex;gap:6px}
.social i{width:24px;height:24px;border-radius:50%;background:#555}
</style>
</head>
<body>
<div class="hero" role="img" aria-label="Photo of a couple embracing in front of a suburban house"></div>

<header class="masthead">
  <div class="brand"><span class="brand-mark"></span>BRAMLEY</div>
  <div class="phone">
    <svg width="32" height="32" viewBox="0 0 32 32"><circle cx="16" cy="16" r="14" fill="none" stroke="#111" stroke-width="2.4"/><path d="M11 9l3 0 1 4-2 1c1 2 3 4 5 5l1-2 4 1 0 3c-1 1-3 1-5 0-3-2-6-5-7-8-1-2 0-3 0-4z" fill="#111"/></svg>
    1-800-555-0142
  </div>
  <div class="search"><span>search...</span><div class="search-btn"><svg width="12" height="12" viewBox="0 0 12 12"><circle cx="5" cy="5" r="3.3" fill="none" stroke="#fff" stroke-width="1.6"/><path d="M7.5 7.5l3 3" stroke="#fff" stroke-width="1.8"/></svg></div></div>
</header>

<nav class="nav"><ul><li class="active">Home</li><li>Properties</li><li>About Us</li></ul></nav>

<h1 class="hero-title">Non Performing  Loans<br>and Investment</h1>

<section class="audiences">
  <div class="audience">
    <h2><svg width="28" height="28" viewBox="0 0 28 28"><circle cx="14" cy="14" r="12" fill="none" stroke="#fff" stroke-width="2.5"/><text x="14" y="20" font-size="17" font-weight="700" text-anchor="middle" fill="#fff" font-family="Open Sans,sans-serif">$</text></svg>Investors</h2>
    <p>Lorem ipsum dolor sit amet, consectetuer adipiscing elit, sed diam nonummy nibh euismod tincidunt ut laoreet dolore magna aliquam erat volutpat.</p>
    <div class="read-more"><svg width="15" height="15" viewBox="0 0 15 15"><circle cx="7.5" cy="7.5" r="6.5" fill="none" stroke="#fff"/><path d="M6 4.5l3 3-3 3" fill="none" stroke="#fff" stroke-width="1.4"/></svg>read more</div>
  </div>
  <div class="audience">
    <h2><svg width="28" height="26" viewBox="0 0 28 26"><path d="M1 3h5l4 13h13l3-10H8" fill="none" stroke="#fff" stroke-width="2.4"/><circle cx="11" cy="21" r="2.3" fill="#fff"/><circle cx="21" cy="21" r="2.3" fill="#fff"/></svg>Buyers</h2>
    <p>Lorem ipsum dolor sit amet, consectetuer adipiscing elit, sed diam nonummy nibh euismod tincidunt ut laoreet dolore magna aliquam erat volutpat.</p>
    <div class="read-more"><svg width="15" height="15" viewBox="0 0 15 15"><circle cx="7.5" cy="7.5" r="6.5" fill="none" stroke="#fff"/><path d="M6 4.5l3 3-3 3" fill="none" stroke="#fff" stroke-width="1.4"/></svg>read more</div>
  </div>
  <div class="audience">
    <h2><svg width="26" height="24" viewBox="0 0 26 24"><path d="M13 1L1 12h4v11h6v-7h4v7h6V12h4z" fill="#fff"/></svg>Sellers</h2>
    <p>Lorem ipsum dolor sit amet, consectetuer adipiscing elit, sed diam nonummy nibh euismod tincidunt ut laoreet dolore magna aliquam erat volutpat.</p>
    <div class="read-more"><svg width="15" height="15" viewBox="0 0 15 15"><circle cx="7.5" cy="7.5" r="6.5" fill="none" stroke="#fff"/><path d="M6 4.5l3 3-3 3" fill="none" stroke="#fff" stroke-width="1.4"/></svg>read more</div>
  </div>
</section>

<main class="welcome">
  <h1>Welcome to <em>Bramley</em></h1>
  <p>Lorem Ipsum is simply dummy text of the printing and typesetting industry. Lorem Ipsum has been the industry's standard dummy text ever since the 1500s, when an unknown printer took a galley of type and scrambled it to make a type specimen book. It has survived not only five centuries, but also the leap into electronic typesetting, remaining essentially unchanged.</p>
  <p>Lorem Ipsum is simply dummy text of the printing and typesetting industry. Lorem Ipsum has been the industry's standard dummy text ever since the 1500s, when an unknown printer took a galley of type and scrambled it to make a type specimen book. When an unknown printer took a galley of type and scrambled it to make a type specimen book.</p>
</main>

<aside class="testimonials">
  <h3>TESTIMONIALS</h3>
  <div class="quote">
    <div class="person"><div class="avatar" role="img" aria-label="Portrait photo of Marcus Hale"></div>
      <div class="who"><b>Marcus Hale</b><br>Managing Director Northvale UK<br>Northvale.co.uk</div></div>
    <blockquote>“Donec sed odio dui. Nulla vitae elit libero, a pharetra augue. Nullam id dolor id nibh</blockquote>
  </div>
  <div class="quote">
    <div class="person"><div class="avatar" role="img" aria-label="Portrait photo of Adrian Pell"></div>
      <div class="who"><b>Adrian Pell</b><br>Technical Director Corvanta International<br>Corvanta.com</div></div>
    <blockquote>“Donec sed odio dui. Nulla vitae elit libero, a pharetra</blockquote>
  </div>
  <div class="grip"></div>
</aside>

<footer class="footer">
  <small>Copyright © 2011 Bramley. All rights reserved.</small>
  <div class="social" aria-label="Social links"><i></i><i></i><i></i><i></i><i></i><i></i><i></i></div>
</footer>
</body>
</html>
```